Stationery Design for Tierhaven

We already have a logo a Logo for our outstanding veterinary hospital. Now we are looking for our future letterhead, business cards and envelopes. We would like to see a design using the color from our logo. Additional color should be limited to grey or a rusty brown. The font should be easy and clearly readable and must be easily available on all computers (to install it in our Management software). The finial design should communicate competence in veterinary medicine, and empathy.

To meet the European regulation (DIN5008) there are a couple mandatory legal informations one the letterhead. We also enclosed a template of exact measurement, which need to be respected according to DIN5008.

Mandatory legal information are (best placed in the footer):
"Tierhaven GmbH & Co KG, Ostrowgasse 417C, 1230 Wien,
Handelsgericht Wien, FN 924615k, GF: Dr. Lukas Brandl
ATU 3148926"
Additional informations needed:
"Tel: +43 1 5849163, Fax: +43 1 5849164, info@tierhaven-example.at, www. tierhaven-example.at"
bank account informations should be included as well. These are:
"Sparkasse Obergruntal, IBAN: AT 58 1111 2222 3333 4444, BIC: SPKTAT4K817"

The Logo should be in the upper right corner. Below that we need a space for informations regarding the responsible veterinarians. There will be 3-5 Names, each of it consisting of 2 lines (see example below). The Names should be highlighted (larger font) compared to the qualifications in the second line.
Tierärztliche Leitung:
Dr. Lukas Brandl
Diplomate ECVS

The contest was startet on the 2nd of may and the deadline was a day later? Why was that so fast? Did I do something wrong? BR

Target Market(s)

dog and cat owner in Austria as welle as referring veterinarians in Austria

Industry/Entity Type

Veterinary

Contact Information for Business Card

One side: Logo
other side:
Dr. Lukas Brandl
Diplomate ECVS
EBVS Specialist of Small Animal Surgery

Tierhaven GmbH&Co KG
Ostrowgasse 417C
1230 Wien

Tel: +43 1 6210000 DW 102
Fax: +43 1 6210000 DW 999
email: lukas.brandl@tierhaven-example.at

Font styles to use
Serif
Sans Serif

Requirements
Must have
• The logo should be given in the upper right. Most of the legal informations should be given in the footer. The upper left Area should be clear, since the recipient address will be placed there.
Colors should be limited to golden, blue and greyscale (two different gereysacales at most).

```html
<!DOCTYPE html>
<html lang="de">
<head>
<meta charset="utf-8">
<title>Tierhaven – Briefpapier</title>
<link href="https://fonts.googleapis.com/css2?family=Roboto:wght@400;500;700&display=swap" rel="stylesheet">
<style>
  :root {
    --navy: #1c2a5a;
    --gold: #d9a21b;
    --ink: #2b2b2b;
    --grey: #8a8a8a;
    --rule: #9a9a9a;
    --backdrop: #d9dadc;
    --paper: #ffffff;
    --mark-grey: #e4e4e9;
    --mark-cream: #fbf5ea;
  }
  * { box-sizing: border-box; margin: 0; padding: 0; }
  html, body { width: 1200px; height: 1200px; overflow: hidden; }
  body {
    background: var(--backdrop);
    font-family: "Roboto", Arial, sans-serif;
    position: relative;
  }
  .letterhead {
    position: absolute;
    left: 197px; top: 30px;
    width: 806px; height: 1140px;
    background: var(--paper);
  }
  .brand {
    position: absolute;
    left: 442px; top: 44px;
    display: flex; align-items: center; gap: 14px;
  }
  .brand-dot {
    width: 82px; height: 82px; border-radius: 50%;
    background: var(--navy);
  }
  .brand-name {
    font-weight: 700; font-size: 30px; color: var(--navy);
    letter-spacing: -0.5px;
  }
  .management {
    position: absolute; left: 440px; top: 175px;
  }
  .management-title {
    font-size: 13.5px; color: var(--ink); margin-bottom: 14px;
  }
  .vet-grid {
    display: grid;
    grid-template-columns: 174px 174px;
    row-gap: 10px;
  }
  .vet-name {
    font-size: 13.5px; font-weight: 500; color: var(--navy); line-height: 15px;
  }
  .vet-role {
    font-size: 13px; color: var(--gold); line-height: 15px;
  }
  .watermark {
    position: absolute; left: 250px; top: 474px;
    width: 312px; height: 312px; border-radius: 50%;
    border: 5px solid var(--mark-cream);
    background: radial-gradient(circle at 45% 40%, var(--mark-grey) 60%, var(--mark-cream) 100%);
    background-clip: content-box;
    padding: 16px;
  }
  .footer-company {
    position: absolute; left: 89px; top: 1002px;
    font-size: 15px; font-weight: 500; color: var(--ink);
  }
  .footer-rule {
    position: absolute; left: 301px; right: 0; top: 1014px;
    height: 1px; background: var(--rule);
  }
  .footer-col {
    position: absolute; top: 1028px;
    font-size: 11.5px; line-height: 15px; color: var(--ink);
  }
  .footer-legal { left: 89px; }
  .footer-contact { left: 336px; }
  .footer-bank { left: 538px; top: 1031px; }
  .footer-divider {
    position: absolute; top: 1029px; width: 1px; height: 62px; background: var(--rule);
  }
  .divider-one { left: 299px; }
  .divider-two { left: 500px; }
  .contact-row { display: flex; align-items: center; gap: 8px; height: 16px; }
  .contact-row svg { width: 11px; height: 11px; fill: var(--grey); flex: none; }
</style>
</head>
<body>
<main class="letterhead">
  <header class="brand">
    <span class="brand-dot"></span>
    <span class="brand-name">Tierhaven</span>
  </header>

  <section class="management">
    <p class="management-title">Tierärztliche Leitung</p>
    <div class="vet-grid">
      <div><p class="vet-name">Dr. Lukas Brandl</p><p class="vet-role">Diplomate ECVS</p></div>
      <div><p class="vet-name">Names of veterinarians</p><p class="vet-role">function in yellow</p></div>
      <div><p class="vet-name">Names of veterinarians</p><p class="vet-role">function in yellow</p></div>
      <div><p class="vet-name">Names of veterinarians</p><p class="vet-role">function in yellow</p></div>
      <div><p class="vet-name">Names of veterinarians</p><p class="vet-role">function in yellow</p></div>
    </div>
  </section>

  <div class="watermark" role="img" aria-label="Faint brand mark: dog and cat silhouettes in a ring"></div>

  <footer>
    <p class="footer-company">Tierhaven GmbH &amp; Co KG</p>
    <div class="footer-rule"></div>
    <div class="footer-col footer-legal">
      Ostrowgasse 417C, 1230 Wien,<br>
      Handelsgericht Wien, FN 924615k,<br>
      GF: Dr. Lukas Brandl<br>
      ATU 3148926
    </div>
    <div class="footer-divider divider-one"></div>
    <div class="footer-col footer-contact">
      <div class="contact-row">
        <svg viewBox="0 0 24 24"><path d="M6.6 10.8a15.1 15.1 0 0 0 6.6 6.6l2.2-2.2c.3-.3.7-.4 1-.2 1.1.4 2.3.6 3.6.6.6 0 1 .4 1 1V20c0 .6-.4 1-1 1A17 17 0 0 1 3 4c0-.6.4-1 1-1h3.5c.6 0 1 .4 1 1 0 1.3.2 2.5.6 3.6.1.3 0 .7-.2 1z"/></svg>
        <span>+43 1 5849163</span>
      </div>
      <div class="contact-row">
        <svg viewBox="0 0 24 24"><path d="M6 2h12v6H6zM3 9h18a1 1 0 0 1 1 1v7h-4v5H6v-5H2v-7a1 1 0 0 1 1-1zm5 7v4h8v-4z"/></svg>
        <span>+43 1 5849164</span>
      </div>
      <div class="contact-row">
        <svg viewBox="0 0 24 24"><path d="M2 5h20v14H2zm2 2v.5l8 5 8-5V7z"/></svg>
        <span>info@tierhaven-example.at</span>
      </div>
      <div class="contact-row">
        <svg viewBox="0 0 24 24"><path d="M12 2a10 10 0 1 0 0 20 10 10 0 0 0 0-20zm0 2c1 1.3 1.8 3.3 2 6h-4c.2-2.7 1-4.7 2-6zM4.1 11h4a15 15 0 0 0 1.2 6.5A8 8 0 0 1 4.1 13zm11.8 0h4a8 8 0 0 1-5.2 6.5 15 15 0 0 0 1.2-6.5zM10 12h4c-.2 3-1 5-2 6.3-1-1.3-1.8-3.3-2-6.3z"/></svg>
        <span>www.tierhaven-example.at</span>
      </div>
    </div>
    <div class="footer-divider divider-two"></div>
    <div class="footer-col footer-bank">
      Sparkasse Obergruntal,<br>
      IBAN: AT 58 1111 2222 3333 4444,<br>
      BIC: SPKTAT4K817
    </div>
  </footer>
</main>
</body>
</html>
```